Australia-Wide Industry Leader Bookkeeping Business Website Design Required

We need a website designed for our 10 year old bookkeeping business, Barwick & Lund. Barwick & Lund has been servicing the local & interstate communities of Australia, providing first-class BAS & Bookkeeping services with a personal touch unmatched by anyone else in the county.

What began 10 years ago as a small business focusing on family, friends and the local community, it has since grown into a well respected business with 95% of their business based solely on word of mouth and personal referrals from around Australia.

We would like to see designs that incorporate our existing brand/logo. The colours to be used on the website should be colours that work well with our logo. The design should communicate maturity, trust and confidence with a Web 2.0 look and feel.

We have produced mockups of the entire website as well as assets used in the mockups. Please reference the attached files. The mockups are an example of all the design elements that we want on each page. Designers are encouraged to use the mockups as a guideline only and for designers to use their own creativity.
Updates

This message is for new graphic designers who are considering commencing work on this project. Thank you for expressing an interest in our project. We would like to inform you that this project is close to completion as we have a number designs under very serious consideration.

We are currently in a position where we are disinterested providing feedback to improve on new designs submitted. We will provide feedback to improve new designs only if the submitted designs are very close to what we want for our website, and will only require 1 or 2 revision rounds to refine before the project completion date we will not work with designers to refine their newly submitted designs.

We feel that it is important for all designers to know the above information as we feel that your time and effort may be better spent working on another project.

Thank you for your understanding.

A big thank you for all the designs submitted. We are now in the process of selecting a design. Please be patient during this process. Thank you.

Target Market(s)

Busy Business Owners

Industry/Entity Type

Small Business

Requirements
Must have
• We require a rectangular "slide show" type feature to serve as a "teaser" to arouse the emotions of our website visitors. Each slide asks a specific question. The questions are:

- Is your paperwork in a mess?
- Do you need to get organised for the end of financial year?
- Are you sick & tired of endless amounts of paperwork & BASs?
- Do you feel frustrated & annoyed because you know your books need to be done?
- Do you lack the time & patience to get your paperwork done?
- Do you wish you had more time to do the things you enjoy doing?
- Contact Barwick & Lund today and we will transform your chaos into order.

Underneath the slide show will be a button to "Call Barwick & Lund Now - 03 5550 1827".

```html
<!DOCTYPE html>
<html lang="en">
<head>
<meta charset="utf-8">
<title>Barwick &amp; Lund – Bookkeeping</title>
<link href="https://fonts.googleapis.com/css2?family=Arimo:wght@400;700&family=Ubuntu:wght@500;700&family=PT+Sans&display=swap" rel="stylesheet">
<style>
:root{
  --text:#555;
  --muted:#9a9a9a;
  --red:#b3161b;
  --tick:#f08c1c;
  --panel:#f7f8f8;
  --panel-border:#cfdddd;
  --rule:#d8d8d8;
  --footer-top:#404040;
  --footer-bottom:#2b2b2b;
  --footer-text:#e4e4e4;
  --footer-muted:#c2c2c2;
}
*{margin:0;padding:0;box-sizing:border-box}
html,body{width:1200px;height:900px;overflow:hidden;background:#fff}
body{position:relative;font-family:"Arimo",Arial,sans-serif;font-size:12px;color:var(--text);letter-spacing:.15px}
.abs{position:absolute}
.line{position:absolute;line-height:16px;white-space:nowrap}
.tick{position:absolute;width:20px;height:16px}
.sub{color:var(--muted)}
.sub::before{content:"";position:absolute;left:-9px;top:4px;border-left:5px solid #aaa;border-top:4px solid transparent;border-bottom:4px solid transparent}
.strong{font-weight:700}
.panel{position:absolute;background:var(--panel);border:1px solid var(--panel-border)}
.panel-title{position:absolute;font-family:"Ubuntu",sans-serif;font-weight:700;color:var(--red);font-size:15px;line-height:20px;letter-spacing:0}
.dashes{position:absolute;height:0;border-top:1px dashed #bbb}
.clip{position:absolute}
.coverage{font-weight:700;color:#666;font-size:12px;line-height:20.5px;white-space:nowrap;letter-spacing:0}
.rule{position:absolute;left:120px;top:591px;width:960px;border-top:1px solid var(--rule)}
.badge{position:absolute}
footer{position:absolute;left:0;top:731px;width:1200px;height:169px;background:linear-gradient(var(--footer-top),var(--footer-bottom));font-family:"PT Sans",sans-serif;letter-spacing:0}
.footer-nav{position:absolute;left:124px;top:32px;color:var(--footer-text);font-size:13px;letter-spacing:.6px}
.footer-nav span{margin:0 9px;color:var(--footer-muted)}
.copyright{position:absolute;left:120px;top:71px;color:var(--footer-muted);font-size:12.5px;letter-spacing:.2px}
.divider{position:absolute;left:786px;top:14px;width:1px;height:136px;background:#555;box-shadow:1px 0 0 #222}
.follow{position:absolute;left:839px;top:32px;color:var(--footer-text);font-size:13px}
.social{position:absolute;top:58px;width:42px;height:42px;border-radius:3px;background:linear-gradient(#f4f4f4,#cfcfcf)}
</style>
</head>
<body>
<svg width="0" height="0" style="position:absolute">
  <defs>
    <symbol id="tick" viewBox="0 0 20 16"><path d="M1 8 L7 13 L19 2 L7 9 Z" fill="var(--tick)"/><path d="M2 8 L7 12" stroke="#c86a08" stroke-width="1"/></symbol>
    <symbol id="paperclip" viewBox="0 0 46 70"><path d="M30 8 C35 0 46 4 42 14 L22 60 C18 70 4 66 8 56 L24 18 C26 12 33 15 31 20 L16 54" fill="none" stroke="#888" stroke-width="2.5" stroke-linecap="round"/></symbol>
  </defs>
</svg>

<section class="intro">
  <svg class="tick" style="left:140px;top:-5px"><use href="#tick"/></svg>
  <div class="line" style="left:167px;top:-5px">The Barwick &amp; Lund team are investors &amp; traders</div>
  <svg class="tick" style="left:140px;top:19px"><use href="#tick"/></svg>
  <div class="line" style="left:167px;top:19px">Extensive business network for your benefit</div>
  <svg class="tick" style="left:140px;top:43px"><use href="#tick"/></svg>
  <div class="line" style="left:167px;top:43px">Sacked by a team of Accountants</div>
  <svg class="tick" style="left:140px;top:67px"><use href="#tick"/></svg>
  <div class="line" style="left:167px;top:67px">We work with a team of elite accountants &amp; wealth creation professionals who coach us monthly in the following:</div>
  <div class="line sub" style="left:182px;top:91px">Asset Protection</div>
  <div class="line sub" style="left:182px;top:115px">Superannuation &amp; Self Managed Superannuation Funds</div>
  <div class="line sub" style="left:182px;top:139px">Property Investing</div>
  <div class="line sub" style="left:182px;top:163px">Tax strategies, tax structures &amp; best tax savings</div>
  <div class="line" style="left:167px;top:187px">We understand just how imnportant it is to help lead &amp; guide our clients from making</div>
  <div class="line" style="left:167px;top:211px">profits to:</div>
  <div class="line sub" style="left:182px;top:235px">Maximising profits</div>
  <div class="line sub" style="left:182px;top:259px">Wealth creation</div>
  <div class="line sub" style="left:182px;top:283px">Tax minimisatien</div>
  <div class="line sub" style="left:182px;top:307px">Asset protection</div>
  <div class="line strong" style="left:167px;top:331px">This is something that other bookkeepers just don't do</div>
</section>

<aside class="panel" style="left:808px;top:-10px;width:273px;height:75px">
  <div class="abs coverage" style="left:16px;top:0">over Victoria, Queensland, NSW &amp; Western<br>Australia, so no matter where you are,<br>we can help!</div>
</aside>

<aside class="panel" style="left:808px;top:102px;width:273px;height:336px">
  <div class="panel-title" style="left:16px;top:11px">Qualifications, Memberships<br>&amp; Partnerships</div>
  <svg class="clip" style="left:226px;top:-12px" width="46" height="70"><use href="#paperclip"/></svg>
  <div class="dashes" style="left:18px;top:68px;width:190px"></div>
  <svg class="tick" style="left:22px;top:88px"><use href="#tick"/></svg><div class="line" style="left:53px;top:88px">Registered NRA BAS Agent</div>
  <svg class="tick" style="left:22px;top:112px"><use href="#tick"/></svg><div class="line" style="left:53px;top:112px">Certificate IV Financial Services</div>
  <svg class="tick" style="left:22px;top:136px"><use href="#tick"/></svg><div class="line" style="left:53px;top:136px">Certificate III Financial Services</div>
  <svg class="tick" style="left:22px;top:160px"><use href="#tick"/></svg><div class="line" style="left:53px;top:160px">Member of Guild of Chartered</div>
  <svg class="tick" style="left:22px;top:184px"><use href="#tick"/></svg><div class="line" style="left:53px;top:184px">Bookkeepers</div>
  <svg class="tick" style="left:22px;top:208px"><use href="#tick"/></svg><div class="line" style="left:53px;top:208px">Platinum Member of Southern</div>
  <svg class="tick" style="left:22px;top:232px"><use href="#tick"/></svg><div class="line" style="left:53px;top:232px">Bookkeepers Guild</div>
  <svg class="tick" style="left:22px;top:256px"><use href="#tick"/></svg><div class="line" style="left:53px;top:256px">Ledgerly Professional Partner</div>
  <svg class="tick" style="left:22px;top:280px"><use href="#tick"/></svg><div class="line" style="left:53px;top:280px">Tax Wise Partners</div>
</aside>

<section class="panel summary" style="left:127px;top:383px;width:656px;height:185px">
  <svg class="abs" style="left:19px;top:7px" width="28" height="28"><rect x="2" y="4" width="20" height="23" rx="2" fill="#d98a1c"/><rect x="6" y="1" width="12" height="6" rx="1" fill="#8a5a14"/><rect x="12" y="8" width="14" height="19" fill="#f4f0e6" stroke="#ccc"/></svg>
  <div class="panel-title" style="left:51px;top:12px">To summarise</div>
  <svg class="clip" style="left:598px;top:-13px" width="46" height="70"><use href="#paperclip"/></svg>
  <div class="dashes" style="left:18px;top:44px;width:570px"></div>
  <div class="line" style="left:25px;top:62px">FREE initial consultation</div>
  <div class="line" style="left:25px;top:86px">Registered BAS Agent #41829-117</div>
  <div class="line" style="left:25px;top:110px">Bookkeeping</div>
  <div class="line" style="left:25px;top:134px">BAS Preparation &amp; Lodgement</div>
  <div class="line" style="left:253px;top:62px">Payroll</div>
  <div class="line" style="left:253px;top:86px">IAS Preparation &amp; Lodgment</div>
  <div class="line" style="left:253px;top:110px">Superannuation &amp; Workcover</div>
  <div class="line" style="left:253px;top:134px">Margin Scheme</div>
  <div class="line" style="left:461px;top:62px">Fuel Tax Credits</div>
  <div class="line" style="left:461px;top:86px">Offsite &amp; onsite bookkeeping</div>
  <div class="line" style="left:461px;top:110px">BookSmith Software &amp; Training</div>
  <div class="line" style="left:461px;top:134px">Australia wide</div>
</section>

<div class="rule"></div>

<section class="partners">
  <svg class="badge" style="left:164px;top:605px" width="63" height="107" role="img" aria-label="Tax Wise Partners badge"><rect x=".5" y=".5" width="62" height="106" fill="#0d3f86" stroke="#0a2c5e"/></svg>
  <svg class="badge" style="left:306px;top:605px" width="93" height="103" role="img" aria-label="Guild of Certified Bookkeepers badge"><rect width="93" height="103" rx="6" fill="#d5454a"/></svg>
  <svg class="badge" style="left:468px;top:612px" width="118" height="94" role="img" aria-label="Coastal Bookkeepers Circle badge"><rect width="118" height="94" fill="#e98a3c"/></svg>
  <svg class="badge" style="left:659px;top:611px" width="53" height="95" role="img" aria-label="Tallyo professional partner badge"><rect width="53" height="95" fill="#1a1a1a"/></svg>
  <svg class="badge" style="left:772px;top:635px" width="250" height="58" role="img" aria-label="National Revenue Authority badge"><rect width="250" height="58" fill="#3a3a3a"/></svg>
</section>

<footer>
  <nav class="footer-nav">Site Map<span>|</span>Privacy<span>|</span>Terms<span>|</span>FAQs<span>|</span>Contact</nav>
  <div class="copyright">The contens of the site are copyright © 2012.&nbsp; Barwick &amp; Lund. All rights reserved.</div>
  <div class="divider"></div>
  <div class="follow">Follow us on:</div>
  <div class="social" style="left:838px" role="img" aria-label="Social network one"></div>
  <div class="social" style="left:891px" role="img" aria-label="Social network two"></div>
  <div class="social" style="left:945px" role="img" aria-label="News feed"></div>
</footer>
</body>
</html>
```